Ridgeline Talent Associates Business Card Design

We need a business card design for our new company - Ridgeline Talent Associates. RLTA is a recruitment firm that focuses on recruiting engineers and geologist for mid-size oil and gas companies. We would like our logo on the business card, which is attached, and we would like the color scheme on business cards to coordinate with our logo.

Industry/Entity Type

Oil And Gas

Contact Information for Business Card

Dana Whitlow, Founder and Managing Partner, dmw@ridgelinetalentco.org, 888.507.3942 (work), 5730915.0600 (cell), 573.642.1907 (fax), www.ridgelinetalentco.org

```html
<!DOCTYPE html>
<html lang="en">
<head>
<meta charset="utf-8">
<title>Ridgeline Talent Associates – Business Card</title>
<link rel="stylesheet" href="https://fonts.googleapis.com/css2?family=Montserrat:wght@400;500;600&display=swap">
<style>
  :root {
    --navy: #3b3a6e;
    --silver: #b9b9bf;
    --silver-light: #dcdce0;
    --paper: #ffffff;
    --ink: #2a2a3a;
    --backdrop: #e9e9ec;
  }
  html, body {
    margin: 0;
    width: 1200px;
    height: 899px;
    overflow: hidden;
    background: var(--backdrop);
  }
  .canvas {
    position: relative;
    width: 1200px;
    height: 899px;
  }
  .card {
    position: absolute;
    left: 100px;
    top: 164px;
    width: 1000px;
    height: 571px;
    border-radius: 44px;
    background: var(--paper);
    overflow: hidden;
    box-shadow: 0 14px 40px rgba(40, 40, 70, 0.18);
    font-family: "Montserrat", sans-serif;
  }
  .card-waves {
    position: absolute;
    inset: 0;
    width: 100%;
    height: 100%;
  }
  .brand {
    position: absolute;
    left: 60px;
    top: 110px;
    display: flex;
    align-items: center;
    gap: 16px;
  }
  .brand-mark {
    width: 44px;
    height: 44px;
    flex: none;
    border-radius: 50%;
    background: var(--navy);
  }
  .brand-name {
    margin: 0;
    font-family: "Montserrat", sans-serif;
    font-weight: 600;
    font-size: 28px;
    letter-spacing: 0.5px;
    color: var(--navy);
    white-space: nowrap;
  }
  .holder {
    position: absolute;
    left: 580px;
    top: 300px;
    width: 330px;
    text-align: center;
  }
  .holder-name {
    margin: 0;
    font-weight: 500;
    font-size: 27px;
    letter-spacing: 1.5px;
    color: var(--ink);
  }
  .holder-title {
    margin: 4px 0 0;
    font-size: 17px;
    color: var(--ink);
  }
  .contacts {
    position: absolute;
    left: 38px;
    top: 318px;
    margin: 0;
    padding: 0;
    list-style: none;
  }
  .contact {
    display: flex;
    align-items: center;
    gap: 12px;
    height: 38px;
    font-size: 15px;
    color: var(--paper);
  }
  .contact-icon {
    width: 22px;
    height: 22px;
    flex: none;
  }
</style>
</head>
<body>
<main class="canvas">
  <section class="card" aria-label="Business card front">
    <svg class="card-waves" viewBox="0 0 1000 571" preserveAspectRatio="none" aria-hidden="true">
      <path d="M0,250 C230,200 430,360 620,420 C780,470 900,440 1000,400 L1000,571 L0,571 Z" fill="var(--silver-light)"/>
      <path d="M0,268 C230,222 430,380 620,440 C780,488 900,462 1000,425 L1000,571 L0,571 Z" fill="var(--silver)"/>
      <path d="M0,285 C230,245 430,402 620,462 C780,510 900,488 1000,455 L1000,571 L0,571 Z" fill="var(--paper)"/>
      <path d="M0,298 C230,262 430,420 620,480 C780,528 900,508 1000,478 L1000,571 L0,571 Z" fill="var(--navy)"/>
    </svg>

    <header class="brand">
      <span class="brand-mark" aria-hidden="true"></span>
      <p class="brand-name">Ridgeline Talent Associates</p>
    </header>

    <div class="holder">
      <p class="holder-name">DANA WHITLOW</p>
      <p class="holder-title">Founder and Managing Partner</p>
    </div>

    <ul class="contacts">
      <li class="contact">
        <svg class="contact-icon" viewBox="0 0 24 24" aria-hidden="true"><circle cx="12" cy="12" r="12" fill="#fff"/><path d="M8.5 6.5l2 2-1.2 1.5c.8 1.7 2 2.9 3.7 3.7l1.5-1.2 2 2-1.3 1.6c-3.8-.5-7-3.7-7.5-7.5z" fill="var(--navy)"/></svg>
        888.507.3942
      </li>
      <li class="contact">
        <svg class="contact-icon" viewBox="0 0 24 24" aria-hidden="true"><circle cx="12" cy="12" r="12" fill="#fff"/><rect x="8.5" y="5.5" width="7" height="13" rx="1.5" fill="var(--navy)"/><rect x="9.7" y="7.2" width="4.6" height="8" fill="#fff"/></svg>
        5730915.0600
      </li>
      <li class="contact">
        <svg class="contact-icon" viewBox="0 0 24 24" aria-hidden="true"><circle cx="12" cy="12" r="12" fill="#fff"/><rect x="6" y="8" width="12" height="8.5" rx="1" fill="var(--navy)"/><path d="M6.5 8.6l5.5 4.2 5.5-4.2" stroke="#fff" stroke-width="1.2" fill="none"/></svg>
        dmw@ridgelinetalentco.org
      </li>
      <li class="contact">
        <svg class="contact-icon" viewBox="0 0 24 24" aria-hidden="true"><circle cx="12" cy="12" r="12" fill="#fff"/><circle cx="12" cy="12" r="6" stroke="var(--navy)" stroke-width="1.4" fill="none"/><path d="M6 12h12M12 6c-2.4 3.5-2.4 8.5 0 12M12 6c2.4 3.5 2.4 8.5 0 12" stroke="var(--navy)" stroke-width="1.2" fill="none"/></svg>
        www.ridgelinetalentco.org
      </li>
      <li class="contact">
        <svg class="contact-icon" viewBox="0 0 24 24" aria-hidden="true"><circle cx="12" cy="12" r="12" fill="#fff"/><path d="M12 5.5a4.3 4.3 0 0 0-4.3 4.3c0 3.2 4.3 8.2 4.3 8.2s4.3-5 4.3-8.2A4.3 4.3 0 0 0 12 5.5z" fill="var(--navy)"/><circle cx="12" cy="9.8" r="1.6" fill="#fff"/></svg>
        410 Ridge Park Drive, Suite 18
      </li>
    </ul>
  </section>
</main>
</body>
</html>
```